New business card design to go with our new logo

just want an eye-catching business card to go with our new logo. We are open to double sided or single sided. Just want it to have the following info on it. Whatever layout you think looks best.

First and Last Name
Title
Phone 801-555-0187
Address 312 W. Larkmoor Avenue Orem UT 84057
Email thecrew@meadowstailandkennel.example

Industry/Entity Type

Business

```html
<!DOCTYPE html>
<html lang="en">
<head>
<meta charset="utf-8">
<title>Meadows Tail and Kennel – Business Card</title>
<link rel="stylesheet" href="https://fonts.googleapis.com/css2?family=Lato:wght@400;700;900&display=swap">
<style>
  :root {
    --brand-blue: #1ea0dc;
    --brand-orange: #f07f1e;
    --ink: #333333;
    --card: #ffffff;
    --backdrop: #ece8e2;
    --mark-light: #d7ecf7;
    --mark-warm: #fbe1c8;
  }
  html, body {
    margin: 0;
    padding: 0;
    width: 1200px;
    height: 800px;
    overflow: hidden;
    background: var(--backdrop);
    font-family: "Lato", Arial, sans-serif;
    color: var(--ink);
  }
  .canvas {
    position: relative;
    width: 1200px;
    height: 800px;
  }
  .card {
    position: absolute;
    top: 245px;
    width: 540px;
    height: 309px;
    background: var(--card);
    box-shadow: 0 6px 18px rgba(0, 0, 0, 0.12);
    overflow: hidden;
  }
  .card--front { left: 30px; }
  .card--back { left: 630px; }

  /* Front: brand name */
  .brand {
    position: absolute;
    inset: 0;
    display: flex;
    flex-direction: column;
    align-items: center;
    justify-content: center;
    gap: 18px;
  }
  .brand__dot {
    width: 56px;
    height: 56px;
    border-radius: 50%;
    background: var(--brand-blue);
  }
  .brand__name {
    margin: 0;
    font-size: 34px;
    font-weight: 900;
    color: var(--brand-orange);
    letter-spacing: 0.5px;
  }

  /* Back: contact details */
  .person {
    position: absolute;
    left: 38px;
    top: 36px;
  }
  .person__name {
    margin: 0;
    font-size: 21px;
    font-weight: 700;
    color: var(--brand-blue);
    letter-spacing: 0.8px;
    text-transform: uppercase;
  }
  .person__title {
    margin: 2px 0 0;
    font-size: 16px;
    font-weight: 400;
    text-transform: uppercase;
    letter-spacing: 0.6px;
  }
  .address {
    position: absolute;
    left: 38px;
    top: 118px;
    margin: 0;
    font-style: normal;
    font-size: 14px;
    line-height: 20px;
  }
  .contacts {
    position: absolute;
    left: 38px;
    top: 186px;
    margin: 0;
    padding: 0;
    list-style: none;
    font-size: 14px;
    line-height: 22px;
  }
  .contacts__item {
    display: flex;
    align-items: center;
    gap: 8px;
  }
  .contacts__icon {
    width: 13px;
    height: 13px;
    flex: none;
  }
  .brand-mark-area {
    position: absolute;
    left: 345px;
    top: 40px;
    width: 160px;
    height: 232px;
    border-radius: 80px 80px 8px 8px;
    background: linear-gradient(180deg, var(--mark-light), var(--mark-warm));
  }
  .edge-bands {
    position: absolute;
    left: 0;
    bottom: 0;
    width: 540px;
    height: 22px;
  }
</style>
</head>
<body>
<main class="canvas">

  <section class="card card--front" aria-label="Card front">
    <div class="brand">
      <span class="brand__dot"></span>
      <p class="brand__name">Meadows Tail and Kennel</p>
    </div>
  </section>

  <section class="card card--back" aria-label="Card back">
    <div class="person">
      <p class="person__name">Dana Whitfield</p>
      <p class="person__title">Manager</p>
    </div>

    <address class="address">312 W. Larkmoor Avenue,<br>Orem UT 84057</address>

    <ul class="contacts">
      <li class="contacts__item">
        <svg class="contacts__icon" viewBox="0 0 16 16" aria-hidden="true">
          <path fill="var(--brand-orange)" d="M3.2 1.2l2.3 2.6-1.3 1.8c.9 2 2.3 3.4 4.2 4.3l1.8-1.3 2.6 2.3-1.3 2.6C6.2 13.2 2.8 9.8 1.2 4.5z"/>
        </svg>
        801-555-0187
      </li>
      <li class="contacts__item">
        <svg class="contacts__icon" viewBox="0 0 16 16" aria-hidden="true">
          <rect x="1" y="3" width="14" height="10" rx="1" fill="var(--brand-orange)"/>
          <path d="M1.5 3.6L8 8.6l6.5-5" fill="none" stroke="#fff" stroke-width="1.3"/>
        </svg>
        thecrew@meadowstailandkennel.example
      </li>
      <li class="contacts__item">
        <svg class="contacts__icon" viewBox="0 0 16 16" aria-hidden="true">
          <g fill="none" stroke="var(--brand-orange)" stroke-width="1.4">
            <circle cx="8" cy="8" r="6.5"/>
            <ellipse cx="8" cy="8" rx="2.8" ry="6.5"/>
            <path d="M1.5 8h13M2.6 4.8h10.8M2.6 11.2h10.8"/>
          </g>
        </svg>
        meadowstailandkennel.example
      </li>
    </ul>

    <div class="brand-mark-area" role="img" aria-label="Brand mark illustration area: a seated dog framed by an orange ring"></div>

    <svg class="edge-bands" viewBox="0 0 540 22" aria-hidden="true">
      <rect x="0" y="14" width="320" height="8" fill="var(--brand-blue)"/>
      <polygon points="310,8 540,8 540,22 300,22" fill="var(--brand-orange)"/>
    </svg>
  </section>

</main>
</body>
</html>
```